Book jacket for Drumlore

We need a book jacket design (hard cover front, back, spine, flaps; soft cover and eBook). for a social psychology book with the general cluelessness (being "out of it") of how people function both in their personal and social lives. This is the third book written by the author, a practicing psychiatrist, and the content centers on a single subject, people's lack of genuine emotional contact, their cluelessness with themselves and with current national and world events.

Target Market(s)

People who want to better understand the state the nation and world is in now, and what they can do about it.

Font styles to use
Serif
Sans Serif

Requirements
Must have
• Bold, eye-catching cover
Nice to have
• Like the idea of separating the title word (drum lore) to better emphasize the concept of lack of contact

```html
<!DOCTYPE html>
<html lang="en">
<head>
<meta charset="utf-8">
<title>Drumlore — Book Jacket</title>
<link href="https://fonts.googleapis.com/css2?family=Bebas+Neue&display=swap" rel="stylesheet">
<style>
  :root {
    --backdrop: #524c51;
    --band-dark: #7f737c;
    --band-light: #ede8ec;
    --title-orange: #f04000;
    --author-red: #b01208;
  }
  html, body {
    margin: 0;
    padding: 0;
    width: 1200px;
    height: 1200px;
    overflow: hidden;
    background: var(--backdrop);
  }
  .book-cover {
    position: absolute;
    left: 300px;
    top: 152px;
    width: 600px;
    height: 896px;
    overflow: hidden;
    font-family: "Bebas Neue", "Arial Narrow", sans-serif;
    box-shadow: 0 10px 30px rgba(0, 0, 0, 0.35);
  }
  .crosswalk {
    position: absolute;
    inset: 0;
    background:
      linear-gradient(180deg, rgba(255,255,255,0.15) 0%, rgba(0,0,0,0) 40%, rgba(40,20,35,0.08) 100%),
      repeating-linear-gradient(180deg,
        var(--band-light) 0px, var(--band-light) 21px,
        var(--band-dark) 21px, var(--band-dark) 41.6px);
    background-position: 0 0, 0 2px;
  }
  .book-title {
    margin: 0;
    font-weight: 400;
  }
  .title-line {
    position: absolute;
    display: block;
    font-size: 314px;
    line-height: 1;
    letter-spacing: 6px;
    color: var(--title-orange);
    mix-blend-mode: multiply;
    white-space: nowrap;
    transform-origin: left top;
    transform: scaleX(0.73);
  }
  .title-line--first {
    left: 46px;
    top: 80px;
  }
  .title-line--second {
    left: 193px;
    top: 320px;
  }
  .author-name {
    position: absolute;
    left: 158px;
    top: 741px;
    margin: 0;
    font-size: 111px;
    line-height: 1;
    color: var(--author-red);
    mix-blend-mode: multiply;
    white-space: nowrap;
    transform-origin: left top;
    transform: scaleX(0.93);
  }
</style>
</head>
<body>
  <main class="book-cover">
    <div class="crosswalk" role="img" aria-label="Aerial photograph of pedestrians walking across a wide striped zebra crossing, tinted in muted mauve tones"></div>
    <h1 class="book-title">
      <span class="title-line title-line--first">DRUM</span>
      <span class="title-line title-line--second">LORE</span>
    </h1>
    <p class="author-name">JANE DOE</p>
  </main>
</body>
</html>
```